Zerova Poultry "The Golden Crate"

I need a business card design and a logo design for my business. It's a delivery business of halal poultry (chicken). I would the business card to include the following information.
-business name: Zerova Poultry
-business tag line: "The Golden Crate"
Name: Tomas Velkor
Contact number: 07812450973
E-mail: zerova_fresh@mailvarn.com
Website: www.zerovapoultry.example
Also need a business logo also included relating to the business.
I would like it professional yet creative. Something original. I want it to have 2 main colours included.
I want it to have a middle Eastern/ Arabic look if possible.
Thanks :)
Target Market(s)
Butchers
Restaurants
Industry/Entity Type
Business
Contact Information for Business Card
Business name: Zerova poultry
Business tag line: "The Golden Crate"
E-mail: zerova_fresh@mailvarn.com
Name: Tomas Velkor
Look and feel

```html
<!DOCTYPE html>
<html lang="en">
<head>
<meta charset="utf-8">
<title>Zerova Poultry — Business Card</title>
<link rel="stylesheet" href="https://fonts.googleapis.com/css2?family=Crimson+Text:wght@600;700&display=swap">
<style>
  :root {
    --backdrop: #2f3b42;
    --card-red: #ad2529;
    --card-black: #0b0b0c;
    --ink-white: #ffffff;
    --rule-white: rgba(255,255,255,0.9);
  }
  * { box-sizing: border-box; margin: 0; padding: 0; }
  html, body {
    width: 1200px; height: 900px; overflow: hidden;
    background: var(--backdrop);
    font-family: "Crimson Text", Georgia, serif;
  }
  .stage {
    width: 1200px; height: 900px;
    display: flex; align-items: center; justify-content: center;
  }
  .business-card {
    position: relative;
    width: 980px; height: 560px;
    background: var(--card-red);
    overflow: hidden;
    color: var(--ink-white);
  }
  .brand {
    position: absolute; left: 0; right: 0; top: 54px;
    text-align: center;
  }
  .brand-name {
    font-weight: 700;
    font-size: 96px;
    line-height: 0.95;
    letter-spacing: 3px;
    color: var(--ink-white);
  }
  .tagline {
    margin-top: 22px;
    display: flex; align-items: center; justify-content: center; gap: 20px;
    font-weight: 600; font-size: 30px; letter-spacing: 2px;
    text-transform: uppercase;
  }
  .tagline-rule {
    width: 110px; height: 2px; background: var(--rule-white);
  }
  .contact-band {
    position: absolute; left: 0; right: 0; bottom: 0;
    height: 160px;
    background: var(--card-black);
  }
  .holder-name {
    position: absolute; left: 0; right: 0; top: 20px;
    text-align: center;
    font-weight: 700; font-size: 31px;
  }
  .contact-row {
    position: absolute; left: 40px; right: 40px; bottom: 32px;
    display: flex; justify-content: space-between; align-items: center;
    font-weight: 700; font-size: 21px;
  }
  .contact-item { display: flex; align-items: center; gap: 10px; white-space: nowrap; }
  .contact-icon { width: 22px; height: 22px; flex: none; }
</style>
</head>
<body>
<main class="stage">
  <section class="business-card">
    <header class="brand">
      <h1 class="brand-name">Zerova<br>Poultry</h1>
      <p class="tagline"><span class="tagline-rule"></span>The Golden Crate<span class="tagline-rule"></span></p>
    </header>

    <footer class="contact-band">
      <p class="holder-name">Tomas Velkor</p>
      <div class="contact-row">
        <span class="contact-item">
          <svg class="contact-icon" viewBox="0 0 22 22" aria-hidden="true">
            <circle cx="11" cy="11" r="9.5" fill="none" stroke="#fff" stroke-width="1.8"/>
            <ellipse cx="11" cy="11" rx="4" ry="9.5" fill="none" stroke="#fff" stroke-width="1.4"/>
            <path d="M1.5 11 H20.5" stroke="#fff" stroke-width="1.4"/>
          </svg>
          www.zerovapoultry.example
        </span>
        <span class="contact-item">
          <svg class="contact-icon" viewBox="0 0 22 22" aria-hidden="true">
            <path d="M5 2 L8 2 L9.5 6.5 L7.5 8.5 C8.8 11 11 13.2 13.5 14.5 L15.5 12.5 L20 14 L20 17 C20 18.7 18.7 20 17 20 C9 20 2 13 2 5 C2 3.3 3.3 2 5 2 Z" fill="#fff"/>
          </svg>
          07812450973
        </span>
        <span class="contact-item">
          <svg class="contact-icon" viewBox="0 0 22 22" aria-hidden="true">
            <rect x="1.5" y="4.5" width="19" height="13" fill="none" stroke="#fff" stroke-width="1.8"/>
            <path d="M1.5 4.5 L11 12 L20.5 4.5" fill="none" stroke="#fff" stroke-width="1.5"/>
          </svg>
          zerova_fresh@mailvarn.com
        </span>
      </div>
    </footer>
  </section>
</main>
</body>
</html>
```